Veranta - Solution provider in business consulting

Veranta is a swiss based company providing solutions for developing markets. The business covers various fields of business consulting, such as supply chain, product costs, quality management and manufacturing management. The Business operates in a efficient, straight and solution oriented manner.
The final design should communicate these characteristics. Asian people as well as as western people shall identify the qualities of the company at first sight.
The customer needs business cards with a simple view but an recognizable design, printed in high quality. Engraved elements such as the globe or simple words are possible.
Available colors are: (RAL)
102/102/102
51/102/102
153/204/153
255/102/51
Font: Calibri
Industry/Entity Type
Business
Look and feel
Each slider illustrates characteristics of the customer's brand and the style your logo design should communicate.

```html
<!DOCTYPE html>
<html lang="en">
<head>
<meta charset="utf-8">
<title>Veranta – Business Card</title>
<link href="https://fonts.googleapis.com/css2?family=Carlito:wght@400;700&display=swap" rel="stylesheet">
<style>
  :root {
    --backdrop: #2b2d31;
    --card-dark: #666666;
    --card-light: #ffffff;
    --ink: #1a1a1a;
    --ink-soft: #555555;
    --brand-grey: #666666;
    --on-dark: #ffffff;
  }
  * { margin: 0; padding: 0; box-sizing: border-box; }
  html, body {
    width: 1200px;
    height: 864px;
    overflow: hidden;
    background: var(--backdrop);
    font-family: "Carlito", "Calibri", sans-serif;
  }
  .canvas {
    position: relative;
    width: 1200px;
    height: 864px;
  }
  .card {
    position: absolute;
    width: 540px;
    height: 310px;
    border-radius: 4px;
    overflow: hidden;
    box-shadow: 0 10px 30px rgba(0,0,0,0.35);
  }

  /* Front side */
  .card--front {
    left: 150px;
    top: 90px;
    background: var(--card-dark);
  }
  .card--front .wordmark {
    position: absolute;
    right: 40px;
    bottom: 46px;
    font-size: 64px;
    font-weight: 400;
    letter-spacing: 1px;
    color: var(--on-dark);
    line-height: 1;
  }

  /* Back side */
  .card--back {
    left: 510px;
    top: 460px;
    background: var(--card-light);
  }
  .card--back .brand {
    position: absolute;
    right: 40px;
    top: 40px;
    display: flex;
    align-items: center;
    gap: 14px;
  }
  .card--back .brand-dot {
    width: 40px;
    height: 40px;
    border-radius: 50%;
    background: var(--brand-grey);
  }
  .card--back .wordmark {
    font-size: 50px;
    font-weight: 400;
    color: var(--brand-grey);
    line-height: 1;
  }
  .person {
    position: absolute;
    left: 32px;
    top: 128px;
  }
  .person-name {
    font-size: 20px;
    font-weight: 700;
    color: var(--ink-soft);
  }
  .person-role {
    font-size: 14px;
    color: var(--ink);
  }
  .contacts {
    position: absolute;
    right: 28px;
    top: 190px;
    list-style: none;
    text-align: right;
  }
  .contacts li {
    display: flex;
    justify-content: flex-end;
    align-items: center;
    gap: 8px;
    font-size: 15px;
    color: var(--ink);
    line-height: 20px;
  }
  .contacts svg {
    width: 12px;
    height: 12px;
    fill: none;
    stroke: var(--ink-soft);
    stroke-width: 1.6;
  }
  .address {
    position: absolute;
    right: 28px;
    bottom: 20px;
    font-size: 15px;
    font-weight: 700;
    color: var(--ink);
  }
</style>
</head>
<body>
<main class="canvas">

  <section class="card card--front" aria-label="Business card front">
    <span class="wordmark">veranta</span>
  </section>

  <section class="card card--back" aria-label="Business card back">
    <div class="brand">
      <span class="wordmark">veranta</span>
      <span class="brand-dot" aria-hidden="true"></span>
    </div>

    <div class="person">
      <p class="person-name">Marten Kohl</p>
      <p class="person-role">CEO</p>
    </div>

    <ul class="contacts">
      <li>+41 79 555 0182
        <svg viewBox="0 0 12 12" aria-hidden="true"><rect x="3" y="1" width="6" height="10" rx="1"/></svg>
      </li>
      <li>+41 71 555 0347
        <svg viewBox="0 0 12 12" aria-hidden="true"><path d="M2 2 L4.5 2 L5.5 4.5 L4 5.5 Q5 7.5 6.5 8 L7.5 6.5 L10 7.5 L10 10 Q5 10.5 2 2 Z"/></svg>
      </li>
      <li>marten.kohl@veranta.ch
        <svg viewBox="0 0 12 12" aria-hidden="true"><rect x="1" y="3" width="10" height="7"/><path d="M1 3 L6 7 L11 3"/></svg>
      </li>
      <li>www.veranta.ch
        <svg viewBox="0 0 12 12" aria-hidden="true"><circle cx="6" cy="6" r="4.5"/><path d="M1.5 6 H10.5 M6 1.5 Q3.5 6 6 10.5 M6 1.5 Q8.5 6 6 10.5"/></svg>
      </li>
    </ul>

    <p class="address">Veranta GmbH Lindenweg 14 9000 Talwil Switzerland</p>
  </section>

</main>
</body>
</html>
```